El Tallercito Brochure

Create a brochure for a new reception venue - El Tallercito
www.El-Tallercito-Salon.com

Here is info it must contain

Please refer to our site for inspiration - I know this is alot of info but ?

El Tallercito Reception Hall
4178C Millbrook Rd, Benicia, CA 707-555-0148
www.El-Tallercito-Salon.com

Located in Benicia, California, we are a new venue that can host a variety of events. We can provide an exceptional space for your next party, reception, quinceañera, birthday party, or meeting! We treat each client with respect and go out of our way to accommodate all of your needs and make your event a success. Conveniently located just off the 680/780 junction, El Tallercito is located in a safe, well-lit area with a large private parking area.

The space comes prepared with everything you need to get your party started – chairs and tables with tablecloths, a well-equipped kitchen, and incredible decorations to set the perfect backdrop to your event! Rent just the Lounge for a more intimate get-together, or add the Main Hall for your large sit-down event.

Lounge – Beautiful 1,600 ft2 entry room featuring large living room with conversation sofa seating for 40+ Sound system  Pass-through bar with seating  Fully-equipped 200 ft2 kitchen with
4-burner gas stove, oven, large double sink, full-size refrigerator, 2 microwaves, and ice machine, plus lots of storage and counter space  Newly-remodeled Men’s and Women’s bathrooms

Main Hall – Spacious 24’x80’ room with seating for up to 160 people  2,000 ft2  72” round tables with chairs, each seating up to 8 guests  DJ stand and Sound system  Atmospheric lighting
_______________________________________
Pricing -
Daytime Parties
Available 8AM-2PM
4-hour minimum

Lounge and Kitchen Only
Fri - Sat - Sun : $80/hr
Mon - Thurs : $60/hr

All Areas: Lounge, Kitchen, Main Hall, and Backyard
Fri - Sat - Sun : $120/hr
Mon - Thurs : $100/hr
___________________________________________
Evening Events
Available 3PM-12AM
5-hour minimum

Lounge and Kitchen Only -
Fri - Sat - Sun : $100/hr
Mon - Thurs : $50/hr

Fri - Sat - Sun : $160/hr
Mon - Thurs : $75/hr
___________________________________________________
Looking for a different time frame, all-day rental, or other special request? Let us know!
We'd be happy to provide you with a custom quote for your event.

```html
<!DOCTYPE html>
<html lang="en">
<head>
<meta charset="utf-8">
<title>El Tallercito Brochure</title>
<link href="https://fonts.googleapis.com/css2?family=Oswald:wght@300;400&family=Barlow+Semi+Condensed:ital,wght@0,400;0,600;1,500&display=swap" rel="stylesheet">
<style>
  :root {
    --paper: #ffffff;
    --taupe: #75655a;
    --ink: #1d1b1b;
    --wine: #542732;
    --text-light: #f3eeea;
    --rule: rgba(255,255,255,0.75);
  }
  * { box-sizing: border-box; margin: 0; padding: 0; }
  html, body { width: 1200px; height: 847px; overflow: hidden; background: var(--paper); }
  .brochure { position: relative; width: 1200px; height: 847px; background: var(--paper);
    font-family: "Barlow Semi Condensed", "Arial Narrow", sans-serif; color: var(--text-light); }
  .panel { position: absolute; top: 0; width: 367px; height: 831px; }
  .panel--about { left: 16px; }
  .panel--why { left: 416px; }
  .panel--prices { left: 816px; }
  .panel-art { position: absolute; inset: 0; }
  .panel-body { position: absolute; left: 0; right: 0; }
  .panel-title { font-family: "Oswald", "Arial Narrow", sans-serif; font-weight: 300;
    font-size: 29px; letter-spacing: 1.5px; text-align: center; color: #fff; line-height: 1; }
  .title-rule { display: block; margin: 6px auto 0; }
  .about .panel-body { top: 314px; padding: 0 18px 0 18px; font-size: 14.5px; line-height: 21px; }
  .intro { padding-left: 17px; margin: 8px 0 18px; }
  .intro b { font-weight: 600; }
  .features { list-style: none; margin-bottom: 39px; }
  .features li { position: relative; padding-left: 19px; }
  .features li svg { position: absolute; left: 0; top: 4px; }
  .why .panel-body { top: 314px; padding: 0 20px; text-align: center; font-size: 14.5px; line-height: 21px; }
  .why p { margin: 0; }
  .why .events { font-weight: 600; letter-spacing: 0.5px; }
  .divider { display: block; margin: 2px auto 3px; }
  .why .title-rule { margin-bottom: 8px; }
  .prices .panel-body { top: 314px; padding: 0 15px; font-size: 14.5px; line-height: 21px; }
  .prices .title-rule { margin-bottom: 4px; }
  .session { text-align: center; }
  .session h3 { font-weight: 600; font-size: 15px; }
  .rate-group { margin-top: 17px; }
  .rate-group h4 { font-weight: 600; font-size: 15px; margin-bottom: 1px; }
  .rate { display: flex; align-items: flex-end; }
  .rate .leader { flex: 1; border-bottom: 1px solid var(--rule); margin: 0 2px 5px; }
  .rate .amount { font-style: italic; font-weight: 500; }
  .evening { margin-top: 19px; }
  .evening + .rate-group { margin-top: 29px; }
</style>
</head>
<body>
<main class="brochure">

  <section class="panel panel--about about">
    <svg class="panel-art" width="367" height="831" viewBox="0 0 367 831">
      <defs>
        <linearGradient id="loungePhoto" x1="0" y1="0" x2="1" y2="1">
          <stop offset="0" stop-color="#e9e4dc"/><stop offset="0.5" stop-color="#8c6f55"/><stop offset="1" stop-color="#3e2a1e"/>
        </linearGradient>
      </defs>
      <rect width="367" height="300" fill="url(#loungePhoto)" role="img" aria-label="Photo of the lounge with pass-through bar, stools and floral wall art"/>
      <path d="M0,196 Q200,270 367,258 L367,300 L0,300 Z" fill="var(--paper)"/>
      <path d="M0,216 Q200,292 367,280 L367,831 L0,831 Z" fill="var(--taupe)"/>
    </svg>
    <div class="panel-body">
      <h2 class="panel-title">ABOUT OUR VENUE</h2>
      <svg class="title-rule" width="330" height="8"><line x1="0" y1="4" x2="330" y2="4" stroke="#fff" stroke-width="1"/><circle cx="4" cy="4" r="2" fill="#fff"/><circle cx="326" cy="4" r="2" fill="#fff"/></svg>
      <p class="intro"><b>Lounge</b> – Beautiful 1,600 ft2 entry room featuring:</p>
      <ul class="features">
        <li><svg width="14" height="14" viewBox="0 0 14 14"><circle cx="7" cy="7" r="6" fill="none" stroke="#fff" stroke-width="1.2"/><path d="M3.8,7.2 L6.2,9.6 L12.5,2" fill="none" stroke="#fff" stroke-width="1.6"/></svg>Large living room with conversation sofa seating for 40+ people;</li>
        <li><svg width="14" height="14" viewBox="0 0 14 14"><circle cx="7" cy="7" r="6" fill="none" stroke="#fff" stroke-width="1.2"/><path d="M3.8,7.2 L6.2,9.6 L12.5,2" fill="none" stroke="#fff" stroke-width="1.6"/></svg>Sound system;</li>
        <li><svg width="14" height="14" viewBox="0 0 14 14"><circle cx="7" cy="7" r="6" fill="none" stroke="#fff" stroke-width="1.2"/><path d="M3.8,7.2 L6.2,9.6 L12.5,2" fill="none" stroke="#fff" stroke-width="1.6"/></svg>Pass-through bar with seating;</li>
        <li><svg width="14" height="14" viewBox="0 0 14 14"><circle cx="7" cy="7" r="6" fill="none" stroke="#fff" stroke-width="1.2"/><path d="M3.8,7.2 L6.2,9.6 L12.5,2" fill="none" stroke="#fff" stroke-width="1.6"/></svg>Fully-equipped 200 ft2 kitchen with 4-burner gas stove, oven, large double sink, full-size refrigerator, 2 microwaves and ice machine, plus lots of storage and counter space;</li>
        <li><svg width="14" height="14" viewBox="0 0 14 14"><circle cx="7" cy="7" r="6" fill="none" stroke="#fff" stroke-width="1.2"/><path d="M3.8,7.2 L6.2,9.6 L12.5,2" fill="none" stroke="#fff" stroke-width="1.6"/></svg>Newly-remodeled Men’s and Women’s bathrooms.</li>
      </ul>
      <p class="intro"><b>Main Hall</b> – Spacious 24’x80’ room with seating for up to 160 people:</p>
      <ul class="features">
        <li><svg width="14" height="14" viewBox="0 0 14 14"><circle cx="7" cy="7" r="6" fill="none" stroke="#fff" stroke-width="1.2"/><path d="M3.8,7.2 L6.2,9.6 L12.5,2" fill="none" stroke="#fff" stroke-width="1.6"/></svg>2,000 ft²;</li>
        <li><svg width="14" height="14" viewBox="0 0 14 14"><circle cx="7" cy="7" r="6" fill="none" stroke="#fff" stroke-width="1.2"/><path d="M3.8,7.2 L6.2,9.6 L12.5,2" fill="none" stroke="#fff" stroke-width="1.6"/></svg>72” round tables with chairs, each seating up to 8 guests;</li>
        <li><svg width="14" height="14" viewBox="0 0 14 14"><circle cx="7" cy="7" r="6" fill="none" stroke="#fff" stroke-width="1.2"/><path d="M3.8,7.2 L6.2,9.6 L12.5,2" fill="none" stroke="#fff" stroke-width="1.6"/></svg>DJ stand and Sound system;</li>
        <li><svg width="14" height="14" viewBox="0 0 14 14"><circle cx="7" cy="7" r="6" fill="none" stroke="#fff" stroke-width="1.2"/><path d="M3.8,7.2 L6.2,9.6 L12.5,2" fill="none" stroke="#fff" stroke-width="1.6"/></svg>Atmospheric lighting.</li>
      </ul>
    </div>
  </section>

  <section class="panel panel--why why">
    <svg class="panel-art" width="367" height="831" viewBox="0 0 367 831">
      <defs>
        <linearGradient id="hallPhoto" x1="0" y1="0" x2="0" y2="1">
          <stop offset="0" stop-color="#8a8276"/><stop offset="0.5" stop-color="#6b5a48"/><stop offset="1" stop-color="#3a2c22"/>
        </linearGradient>
      </defs>
      <path d="M0,0 H367 V284 Q183,262 0,284 Z" fill="url(#hallPhoto)" role="img" aria-label="Photo of the lounge sofas under paper lanterns beside tall windows"/>
      <path d="M0,300 Q183,284 367,300 L367,831 L0,831 Z" fill="var(--ink)"/>
    </svg>
    <div class="panel-body">
      <h2 class="panel-title">WHY CHOOSE US?</h2>
      <svg class="title-rule" width="1" height="14"></svg>
      <p>Located in Benicia, California, we are a new venue that can host a variety of events. We provide an exceptional space for your</p>
      <p class="events">NEXT PARTY, RECEPTION, QUINCEAÑERA, BIRTHDAY PARTY OR MEETING!</p>
      <svg class="divider" width="326" height="10"><line x1="0" y1="5" x2="326" y2="5" stroke="#fff" stroke-width="1"/><rect x="2" y="2" width="6" height="6" fill="#fff"/><rect x="318" y="2" width="6" height="6" fill="#fff"/></svg>
      <p>We treat each client with respect and go out of our way to accommodate all of your needs and make your event a success.</p>
      <svg class="divider" width="326" height="10"><line x1="0" y1="5" x2="326" y2="5" stroke="#fff" stroke-width="1"/><rect x="2" y="2" width="6" height="6" fill="#fff"/><rect x="318" y="2" width="6" height="6" fill="#fff"/></svg>
      <p>Conveniently located just off the 680/780 junction, El Tallercito is located in a safe, well-lit area with a large private parking space.</p>
      <svg class="divider" width="326" height="10"><line x1="0" y1="5" x2="326" y2="5" stroke="#fff" stroke-width="1"/><rect x="2" y="2" width="6" height="6" fill="#fff"/><rect x="318" y="2" width="6" height="6" fill="#fff"/></svg>
      <p>The space comes prepared with everything you need to get your party started: chairs and tables with tablecloths, a well-equipped kitchen, and incredible decorations to set the perfect backdrop to your event! Rent just the Lounge for a more intimate get-together, or add the Main Hall for your large sit-down event.</p>
    </div>
  </section>

  <section class="panel panel--prices prices">
    <svg class="panel-art" width="367" height="831" viewBox="0 0 367 831">
      <defs>
        <linearGradient id="buffetPhoto" x1="0" y1="0" x2="1" y2="1">
          <stop offset="0" stop-color="#8b7766"/><stop offset="0.6" stop-color="#c7b8a6"/><stop offset="1" stop-color="#5a4636"/>
        </linearGradient>
      </defs>
      <rect width="367" height="300" fill="url(#buffetPhoto)" role="img" aria-label="Photo of a buffet table with fresh food and flowers in the lounge"/>
      <path d="M0,270 Q180,262 367,185 L367,300 L0,300 Z" fill="var(--paper)"/>
      <path d="M0,292 Q180,282 367,205 L367,831 L0,831 Z" fill="var(--wine)"/>
    </svg>
    <div class="panel-body">
      <h2 class="panel-title">PRICES</h2>
      <svg class="title-rule" width="330" height="8"><line x1="0" y1="4" x2="330" y2="4" stroke="#fff" stroke-width="1"/><circle cx="4" cy="4" r="2" fill="#fff"/><circle cx="326" cy="4" r="2" fill="#fff"/></svg>
      <div class="session">
        <h3>Daytime Parties</h3>
        <p>Available 8AM-2PM. 4-hour minimum</p>
      </div>
      <div class="rate-group">
        <h4>All Areas: Lounge, Kitchen, Main Hall and Backyard</h4>
        <div class="rate"><span>Fri - Sat - Sun :</span><span class="leader"></span><span class="amount">$120/hr</span></div>
        <div class="rate"><span>Mon - Thurs :</span><span class="leader"></span><span class="amount">$100/hr</span></div>
      </div>
      <div class="rate-group">
        <h4>Lounge and Kitchen Only</h4>
        <div class="rate"><span>Fri - Sat - Sun :</span><span class="leader"></span><span class="amount">$80/hr</span></div>
        <div class="rate"><span>Mon - Thurs :</span><span class="leader"></span><span class="amount">$60/hr</span></div>
      </div>
      <div class="session evening">
        <h3>Evening Events</h3>
        <p>Available 3PM-12AM. 5-hour minimum</p>
      </div>
      <div class="rate-group">
        <h4>Lounge and Kitchen Only</h4>
        <div class="rate"><span>Fri - Sat - Sun :</span><span class="leader"></span><span class="amount">$100/hr</span></div>
        <div class="rate"><span>Mon - Thurs :</span><span class="leader"></span><span class="amount">$50/hr</span></div>
      </div>
      <div class="rate-group">
        <h4>All Areas: Lounge, Kitchen, Main Hall and Backyard</h4>
        <div class="rate"><span>Fri - Sat - Sun :</span><span class="leader"></span><span class="amount">$160/hr</span></div>
        <div class="rate"><span>Mon - Thurs :</span><span class="leader"></span><span class="amount">$75/hr</span></div>
      </div>
    </div>
  </section>

</main>
</body>
</html>
```